out of the box Business Card Design for a Manufacturer / Distributor

We are a manufarturer and distributor of products.
the company name is VORTANI (Pic attached)

the picture is NOT a must have on the business Card.

the Business Card should look really professional and/or special, so out of the box thinking is welcome.

there should be 2 Adresses on the Business Card for Main and Branch Office.
Email Adress, homepage, Name is required
NO Phone Number

Our working field:
Private Labeling
high Quality Production
direct distribution
warehousing
trademark registration
legal support

Main Office:
Kornblumenweg 14
08352 Haselbrück
Germany

Branch Office:
Daska Lane
Zaranpur
Pakistan

Names:
Lukas Feldhaus (Owner)
Imran Qureshi (Owner)

Email:
lukas@vortani-example.com
imran@vortani-example.com

homepage:
vortani-example.com

Industry/Entity Type

Manufacturer Distributer

Contact Information for Business Card

Vortani

Requirements
Must have
• Names, both office Adresses, email, homepage
Should not have
• Phone Number

```html
<!DOCTYPE html>
<html lang="en">
<head>
<meta charset="utf-8">
<title>Vortani Business Card</title>
<link rel="stylesheet" href="https://fonts.googleapis.com/css2?family=Source+Sans+3:wght@400;500&display=swap">
<style>
  :root {
    --stage: #b3b3b3;
    --ink: #4d4d4d;
    --paper: #ffffff;
    --text: #3a3a3a;
  }
  * { margin: 0; padding: 0; box-sizing: border-box; }
  html, body { width: 1000px; height: 1200px; overflow: hidden; }
  body {
    background: var(--stage);
    font-family: "Source Sans 3", "Myriad Pro", Arial, sans-serif;
    position: relative;
  }
  .card {
    position: absolute;
    left: 51px;
    width: 898px;
    height: 538px;
    background: var(--paper);
    overflow: hidden;
  }
  .card--front { top: 44px; }
  .card--back { top: 617px; }
  .card__waves { position: absolute; inset: 0; width: 100%; height: 100%; }
  .card__waves path { fill: var(--ink); }

  .brand-name {
    position: absolute;
    font-size: 63px;
    font-weight: 400;
    letter-spacing: 0.5px;
    line-height: 1;
  }
  .card--front .brand-name { left: 146px; top: 146px; color: var(--ink); }
  .card--back .brand-name { left: 190px; top: 248px; color: var(--paper); }

  .contact {
    position: absolute;
    left: 45px;
    top: 271px;
    color: var(--text);
    font-size: 30px;
    line-height: 37px;
  }
  .contact__row { display: flex; align-items: center; white-space: nowrap; }
  .contact__row--indent { padding-left: 38px; }
  .icon {
    width: 26px; height: 26px; margin-right: 12px; flex: none;
    background: var(--ink); border-radius: 3px;
    display: inline-flex; align-items: center; justify-content: center;
  }
  .icon svg { width: 20px; height: 20px; }
  .contact .icon { width: 27px; height: 27px; margin-left: 4px; margin-right: 7px; }

  .offices {
    position: absolute;
    left: 583px;
    color: var(--text);
    font-size: 30px;
    line-height: 37px;
  }
  .offices--branch { top: 96px; }
  .offices--main { top: 277px; }
  .offices__title { display: flex; align-items: center; }
  .offices__title .icon { margin-right: 12px; }
  .offices__line { padding-left: 39px; white-space: nowrap; }

  .services {
    position: absolute;
    left: 525px;
    top: 118px;
    list-style: none;
    color: var(--paper);
    font-size: 27px;
    line-height: 52px;
  }
  .services li { display: flex; align-items: center; }
  .services li::before {
    content: ""; width: 10px; height: 10px; border-radius: 50%;
    background: var(--paper); margin-right: 11px;
  }
</style>
</head>
<body>

<section class="card card--front">
  <svg class="card__waves" viewBox="0 0 1062 636" preserveAspectRatio="none" aria-hidden="true">
    <path d="M0,0 H1062 V76 C900,30 760,40 560,62 C360,84 200,108 0,78 Z"/>
    <path d="M0,560 C180,590 340,585 560,560 C760,536 900,525 1062,560 V636 H0 Z"/>
  </svg>
  <div class="brand-name">VORTANI</div>

  <div class="contact">
    <div class="contact__row">Lukas Feldhaus (Owner)</div>
    <div class="contact__row">Imran Qureshi (Owner)</div>
    <div class="contact__row">
      <span class="icon"><svg viewBox="0 0 20 20"><rect x="3" y="5" width="14" height="10" fill="none" stroke="#fff" stroke-width="1.4"/><path d="M3,5 L10,11 L17,5 M3,15 L8,10 M17,15 L12,10" fill="none" stroke="#fff" stroke-width="1.2"/></svg></span>
      lukas@vortani-example.com
    </div>
    <div class="contact__row contact__row--indent">imran@vortani-example.com</div>
    <div class="contact__row">
      <span class="icon"><svg viewBox="0 0 20 20"><g fill="none" stroke="#fff" stroke-width="1.2"><circle cx="10" cy="10" r="7"/><ellipse cx="10" cy="10" rx="3" ry="7"/><path d="M3,10 H17 M4.5,6 H15.5 M4.5,14 H15.5"/></g></svg></span>
      vortani-example.com
    </div>
  </div>

  <div class="offices offices--branch">
    <div class="offices__title">
      <span class="icon"><svg viewBox="0 0 20 20"><path d="M10,2 C6.5,2 4.5,4.6 4.5,7.5 C4.5,11 10,16 10,16 C10,16 15.5,11 15.5,7.5 C15.5,4.6 13.5,2 10,2 Z" fill="none" stroke="#fff" stroke-width="1.4"/><circle cx="10" cy="7.5" r="2" fill="#fff"/><path d="M6,18 H14" stroke="#fff" stroke-width="1.4"/></svg></span>
      Branch Office:
    </div>
    <div class="offices__line">Daska Lane</div>
    <div class="offices__line">Zaranpur</div>
    <div class="offices__line">Pakistan</div>
  </div>

  <div class="offices offices--main">
    <div class="offices__title">
      <span class="icon"><svg viewBox="0 0 20 20"><path d="M10,2 C6.5,2 4.5,4.6 4.5,7.5 C4.5,11 10,16 10,16 C10,16 15.5,11 15.5,7.5 C15.5,4.6 13.5,2 10,2 Z" fill="none" stroke="#fff" stroke-width="1.4"/><circle cx="10" cy="7.5" r="2" fill="#fff"/><path d="M6,18 H14" stroke="#fff" stroke-width="1.4"/></svg></span>
      Main Office:
    </div>
    <div class="offices__line">Kornblumenweg 14</div>
    <div class="offices__line">08352 Haselbrück</div>
    <div class="offices__line">Germany</div>
  </div>
</section>

<section class="card card--back">
  <svg class="card__waves" viewBox="0 0 1062 636" preserveAspectRatio="none" aria-hidden="true">
    <path d="M0,76 C200,50 360,35 560,45 C760,56 900,95 1062,72 V552 C900,510 760,505 560,525 C360,546 180,580 0,560 Z"/>
  </svg>
  <div class="brand-name">VORTANI</div>
  <ul class="services">
    <li>Private labeling</li>
    <li>High quality production</li>
    <li>Direct distribution</li>
    <li>Warehousing</li>
    <li>Trademark registration</li>
    <li>Legal support</li>
  </ul>
</section>

</body>
</html>
```